New bussiness card, using company logo.
Lachlan Voss
Manager/Director
Birch Property Developments
Po Box 4657
Thuringowa Central
Qld
0455 386 218
lachlan@birchpropertydevelopments
eye catching, vibrant colours, professional

```html
<!DOCTYPE html>
<html lang="en">
<head>
<meta charset="utf-8">
<title>Birch Property Developments – Business Card</title>
<link href="https://fonts.googleapis.com/css2?family=Roboto+Condensed:wght@700&display=swap" rel="stylesheet">
<style>
  :root {
    --page: #ffffff;
    --carbon-dark: #141414;
    --carbon-mid: #262626;
    --orange: #ff9600;
    --orange-ink: #c0500a;
    --orange-rule: #ffb84d;
    --brand-green: #3fca3a;
  }
  html, body {
    margin: 0;
    width: 1200px;
    height: 1200px;
    overflow: hidden;
    background: var(--page);
    font-family: "Roboto Condensed", "Arial Narrow", sans-serif;
  }
  .canvas { position: relative; width: 1200px; height: 1200px; }
  .card {
    position: absolute;
    left: 271px;
    width: 648px;
    height: 384px;
    overflow: hidden;
    background: linear-gradient(135deg, var(--carbon-mid), var(--carbon-dark) 55%, var(--carbon-mid));
  }
  .card--front { top: 151px; }
  .card--back { top: 679px; }

  .front__band {
    position: absolute;
    left: 0; right: 0;
    top: 53px; height: 288px;
    background: var(--orange);
  }
  .front__tab {
    position: absolute;
    left: 0; top: 125px;
    width: 29px; height: 144px;
    background: var(--carbon-dark);
    border-radius: 0 14px 14px 0;
  }
  .brand-plate {
    position: absolute;
    left: 41px; top: 0;
    width: 312px; height: 96px;
    background: var(--carbon-dark);
    border-radius: 0 0 22px 22px;
    display: flex; align-items: center; justify-content: center; gap: 12px;
  }
  .brand-mark {
    width: 18px; height: 18px;
    background: var(--brand-green);
    flex: none;
  }
  .brand-name {
    color: var(--brand-green);
    font-weight: 700;
    font-size: 22px;
    line-height: 1.05;
    letter-spacing: 0.5px;
    text-transform: uppercase;
  }
  .contact { color: var(--orange-ink); font-weight: 700; text-transform: uppercase; position: absolute; margin: 0; }
  .contact__email { left: 41px; top: 100px; font-size: 21px; letter-spacing: 0.3px; }
  .contact__name { left: 41px; top: 124px; font-size: 50px; line-height: 1; letter-spacing: 1px; }
  .contact__title { left: 79px; top: 186px; font-size: 25px; }
  .contact__rule {
    position: absolute;
    left: 41px; right: 0; top: 221px;
    height: 2px;
    background: var(--orange-rule);
  }
  .contact__phone { right: 22px; top: 295px; font-size: 25px; letter-spacing: 1px; }

  .back__brand {
    position: absolute;
    inset: 0;
    display: flex; align-items: center; justify-content: center; gap: 16px;
  }
  .back__brand .brand-name { font-size: 34px; }
  .back__brand .brand-mark { width: 26px; height: 26px; }
</style>
</head>
<body>
<main class="canvas">
  <section class="card card--front" aria-label="Business card front">
    <div class="front__band"></div>
    <div class="front__tab"></div>
    <div class="brand-plate">
      <span class="brand-mark"></span>
      <span class="brand-name">Birch Property<br>Developments</span>
    </div>
    <p class="contact contact__email">lachlan@birchpropertydevelopments</p>
    <h1 class="contact contact__name">Lachlan Voss</h1>
    <p class="contact contact__title">Manager/Director</p>
    <div class="contact__rule"></div>
    <p class="contact contact__phone">Phone : 0455 386 218</p>
  </section>

  <section class="card card--back" aria-label="Business card back">
    <div class="back__brand">
      <span class="brand-mark"></span>
      <span class="brand-name">Birch Property<br>Developments</span>
    </div>
  </section>
</main>
</body>
</html>
```